Maison Corvel

I am actually making my own traditional french food.
Everything is homemade with passion.
I make differente terrines, jams, macaroons, rillettes and much more
I do as well cocktail party and catering
Updates

Hello everyone,

On the business card I would like to see appear if it's possible these following informations: traditional french food, cocktail party and catering.

Industry/Entity Type

Catering

```html
<!DOCTYPE html>
<html lang="en">
<head>
<meta charset="utf-8">
<title>Maison Corvel – Business Card</title>
<link href="https://fonts.googleapis.com/css2?family=Marcellus&display=swap" rel="stylesheet">
<style>
  :root {
    --backdrop: #e9e9e9;
    --paper: #ffffff;
    --tricolour-blue: #2e3192;
    --tricolour-red: #c1202f;
    --ink: #1a1a1a;
  }
  * { margin: 0; padding: 0; box-sizing: border-box; }
  html, body {
    width: 1200px; height: 1000px; overflow: hidden;
    background: var(--backdrop);
    font-family: "Marcellus", Georgia, serif;
  }
  .card {
    position: absolute; left: 251px; width: 698px; height: 400px;
    background: var(--paper);
  }
  .card--front { top: 49px; }
  .card--back { top: 549px; }

  .frame { position: absolute; }
  .frame--blue-top { left: 0; top: 0; width: 236px; height: 14px; background: var(--tricolour-blue); }
  .frame--blue-side { left: 0; top: 0; width: 14px; height: 400px; background: var(--tricolour-blue); }
  .frame--blue-bottom { left: 0; bottom: 0; width: 236px; height: 14px; background: var(--tricolour-blue); }
  .frame--red-top { right: 0; top: 0; width: 236px; height: 14px; background: var(--tricolour-red); }
  .frame--red-side { right: 0; top: 0; width: 14px; height: 400px; background: var(--tricolour-red); }
  .frame--red-bottom { right: 0; bottom: 0; width: 236px; height: 14px; background: var(--tricolour-red); }

  .identity {
    position: absolute; display: flex; flex-direction: column; align-items: center;
  }
  .card--front .identity { left: 0; right: 0; top: 148px; }
  .card--back .identity { left: 20px; width: 270px; top: 172px; }

  .brand {
    display: flex; align-items: center;
    color: var(--ink); text-transform: uppercase; white-space: nowrap;
  }
  .brand__dot { border-radius: 50%; background: var(--tricolour-red); flex: none; }
  .card--front .brand { gap: 16px; font-size: 40px; letter-spacing: 1px; }
  .card--front .brand__dot { width: 28px; height: 28px; }
  .card--back .brand { gap: 8px; font-size: 20px; }
  .card--back .brand__dot { width: 14px; height: 14px; }

  .services {
    color: var(--tricolour-blue); text-align: center; white-space: nowrap;
    border-top: 2px solid var(--ink);
  }
  .card--front .services { margin-top: 14px; padding-top: 12px; font-size: 17px; letter-spacing: 2px; }
  .card--back .services { margin-top: 8px; padding-top: 7px; font-size: 12px; letter-spacing: 0.5px; line-height: 1.5; }

  .divider {
    position: absolute; left: 300px; top: 96px; width: 2px; height: 210px;
    background: var(--tricolour-blue);
  }
  .contact { position: absolute; left: 335px; top: 94px; font-variant-numeric: lining-nums; }
  .contact__name { font-size: 30px; color: var(--tricolour-red); letter-spacing: 1px; line-height: 1; }
  .contact__abn { margin: 4px 0 0 69px; font-size: 13px; color: var(--tricolour-blue); letter-spacing: 0.5px; }
  .contact__line {
    position: absolute; left: 0; display: flex; align-items: center; gap: 26px;
    font-size: 23px; color: var(--tricolour-red); white-space: nowrap;
  }
  .contact__line--email { top: 94px; letter-spacing: 2px; }
  .contact__line--phone { top: 186px; letter-spacing: 5px; }
  .contact__icon { width: 36px; height: 24px; flex: none; }
</style>
</head>
<body>
  <section class="card card--front">
    <div class="frame frame--blue-top"></div>
    <div class="frame frame--blue-side"></div>
    <div class="frame frame--blue-bottom"></div>
    <div class="frame frame--red-top"></div>
    <div class="frame frame--red-side"></div>
    <div class="frame frame--red-bottom"></div>
    <div class="identity">
      <div class="brand"><span class="brand__dot"></span>Maison Corvel</div>
      <p class="services">Traditional French food · Cocktail party · Catering</p>
    </div>
  </section>

  <section class="card card--back">
    <div class="frame frame--blue-top"></div>
    <div class="frame frame--blue-side"></div>
    <div class="frame frame--blue-bottom"></div>
    <div class="frame frame--red-top"></div>
    <div class="frame frame--red-side"></div>
    <div class="frame frame--red-bottom"></div>

    <div class="identity">
      <div class="brand"><span class="brand__dot"></span>Maison Corvel</div>
      <p class="services">Traditional French food<br>Cocktail party · Catering</p>
    </div>
    <div class="divider"></div>

    <div class="contact">
      <p class="contact__name">Julien Morvan</p>
      <p class="contact__abn">ABN: 38201947615</p>

      <p class="contact__line contact__line--email">
        <svg class="contact__icon" viewBox="0 0 36 24" aria-hidden="true">
          <rect x="0" y="2" width="36" height="20" fill="#2e3192"/>
          <polyline points="1,3 18,15 35,3" fill="none" stroke="#fff" stroke-width="2"/>
          <line x1="1" y1="21" x2="13" y2="11" stroke="#fff" stroke-width="1.5"/>
          <line x1="35" y1="21" x2="23" y2="11" stroke="#fff" stroke-width="1.5"/>
        </svg>
        jmorvan@corvel.fr
      </p>

      <p class="contact__line contact__line--phone">
        <svg class="contact__icon" viewBox="0 0 36 24" aria-hidden="true">
          <path d="M2 8 Q18 -2 34 8 L31 11 L25 9 L24 6 Q18 4 12 6 L11 9 L5 11 Z" fill="#2e3192"/>
          <path d="M9 11 L13 8 L23 8 L27 11 L30 23 L6 23 Z" fill="#2e3192"/>
          <circle cx="18" cy="16" r="3.5" fill="#fff"/>
        </svg>
        0491570263
      </p>
    </div>
  </section>
</body>
</html>
```